NEW Modern Sleek Business Card for VR Language Startup

Our startup is using VR to lead the next wave of world language education. We need a two-sided business card that introduces the larger organization (Quorvel Language Inc) and our contact info on one side and shows the product, Lumidrasca, on the other side.

Side 1 (contact info)= Quorvel Logo and Contact info (name, title, phone, email)

Side 2 (product)= Lumidrasc logo, text, and website
Text= Culturally Immersive Language Learning Games
Website= www.lumidrasc.example

Target Market(s)

Education, Technology

Contact Information for Business Card

Contact info will be updated upon approval of the design. For now, put this as a placeholder.

Perry Hollins
Founder & CEO
phollins@mailtrove.example
(555)-014-2736

Font styles to use
Other font styles liked:
• Gibson and Century Gothic are the brand fonts

Requirements
Nice to have
• I would love to see cohesion between the design and colors of the two logos. I have attached a few business card designs that I like, so you can get a feel for my preferred style.

```html
<!DOCTYPE html>
<html lang="en">
<head>
<meta charset="utf-8">
<title>Quorvel Language – Business Card</title>
<link href="https://fonts.googleapis.com/css2?family=Montserrat:wght@500;600;700&family=Questrial&display=swap" rel="stylesheet">
<style>
  :root {
    --backdrop: #1d1f24;
    --card-black: #121214;
    --panel-black: #1a1a1c;
    --card-white: #ffffff;
    --text-white: #ffffff;
    --text-grey: #b9b9bf;
    --text-dark: #3a3a3e;
    --orange: #ffb347;
    --red: #ff4f6d;
    --purple: #9b5cff;
    --blue: #3fc8f4;
    --brand-gradient: linear-gradient(90deg, var(--orange), var(--red) 35%, var(--purple) 70%, var(--blue));
  }
  * { box-sizing: border-box; margin: 0; padding: 0; }
  html, body {
    width: 1200px; height: 900px; overflow: hidden;
    background: var(--backdrop);
    font-family: "Questrial", "Century Gothic", sans-serif;
  }
  .stage {
    width: 1200px; height: 900px;
    display: flex; flex-direction: column; align-items: center; justify-content: center;
    gap: 56px;
  }
  .card {
    position: relative;
    width: 620px; height: 354px;
    border-radius: 26px;
    overflow: hidden;
    box-shadow: 0 18px 40px rgba(0,0,0,.45);
  }

  /* ---------- Contact side ---------- */
  .card--contact { background: var(--card-black); }
  .contact__artwork {
    position: absolute; left: -40px; top: -30px;
    width: 330px; height: 400px;
    border-radius: 46% 54% 40% 60% / 50% 46% 54% 50%;
    background: linear-gradient(160deg, var(--orange) 0%, var(--red) 35%, var(--purple) 62%, var(--blue) 100%);
  }
  .brand {
    display: flex; align-items: center; gap: 10px;
    font-family: "Montserrat", sans-serif;
    font-weight: 600;
    color: var(--text-white);
    text-transform: uppercase;
    letter-spacing: .18em;
  }
  .brand__dot {
    width: 26px; height: 26px; border-radius: 50%;
    background: var(--brand-gradient);
    flex: none;
  }
  .contact__brand { position: absolute; right: 34px; top: 40px; font-size: 17px; }
  .contact__details {
    position: absolute; right: 34px; bottom: 40px;
    text-align: right; color: var(--text-white);
  }
  .contact__name {
    font-family: "Montserrat", sans-serif; font-weight: 700;
    font-size: 24px; letter-spacing: .01em;
  }
  .contact__title { font-size: 12px; color: var(--text-grey); margin-top: 2px; margin-bottom: 18px; }
  .contact__line {
    display: flex; align-items: center; justify-content: flex-end; gap: 10px;
    font-size: 13px; margin-top: 8px;
  }
  .contact__icon { width: 16px; height: 16px; flex: none; }

  /* ---------- Product side ---------- */
  .card--product { background: var(--card-white); }
  .product__panel {
    position: absolute; left: 34px; right: 0; top: 0; height: 262px;
    background: var(--panel-black);
    border-radius: 0 0 0 22px;
    display: flex; flex-direction: column; align-items: center; justify-content: center;
    gap: 18px;
  }
  .product__brand { font-size: 26px; letter-spacing: .2em; }
  .product__brand .brand__dot { width: 34px; height: 34px; }
  .product__tagline {
    font-size: 15px; letter-spacing: .02em;
    background: var(--brand-gradient);
    -webkit-background-clip: text; background-clip: text;
    color: transparent;
  }
  .product__stripe {
    position: absolute; width: 34px; height: 92px;
    background: linear-gradient(180deg, var(--blue), var(--purple) 45%, var(--red) 80%, var(--orange));
  }
  .product__stripe--left { left: 0; top: 0; height: 40px; }
  .product__stripe--right { right: 0; bottom: 0; height: 92px; width: 22px; }
  .product__website {
    position: absolute; left: 0; right: 0; bottom: 32px;
    text-align: center; font-size: 15px; color: var(--text-dark); letter-spacing: .03em;
  }
</style>
</head>
<body>
<main class="stage">

  <section class="card card--contact">
    <div class="contact__artwork" role="img" aria-label="Gradient profile illustration of a head with circuit nodes"></div>
    <div class="brand contact__brand"><span class="brand__dot"></span>Quorvel Language</div>
    <div class="contact__details">
      <p class="contact__name">Perry Hollins</p>
      <p class="contact__title">Founder &amp; CEO</p>
      <p class="contact__line">(555)-014-2736
        <svg class="contact__icon" viewBox="0 0 24 24" fill="none" stroke="#ff4f6d" stroke-width="2" stroke-linecap="round" stroke-linejoin="round"><path d="M22 16.9v3a2 2 0 0 1-2.2 2 19.8 19.8 0 0 1-8.6-3.1 19.5 19.5 0 0 1-6-6A19.8 19.8 0 0 1 2.1 4.2 2 2 0 0 1 4.1 2h3a2 2 0 0 1 2 1.7c.1.9.4 1.8.7 2.7a2 2 0 0 1-.5 2.1L8 9.8a16 16 0 0 0 6 6l1.3-1.3a2 2 0 0 1 2.1-.4c.9.3 1.8.6 2.7.7a2 2 0 0 1 1.7 2z"/></svg>
      </p>
      <p class="contact__line">phollins@mailtrove.example
        <svg class="contact__icon" viewBox="0 0 24 24"><rect x="2" y="5" width="20" height="14" rx="2" fill="#9b5cff"/><path d="M2 7l10 6 10-6" fill="none" stroke="#ffb347" stroke-width="2"/></svg>
      </p>
    </div>
  </section>

  <section class="card card--product">
    <div class="product__stripe product__stripe--left"></div>
    <div class="product__panel">
      <div class="brand product__brand"><span class="brand__dot"></span>Quorvel Language</div>
      <p class="product__tagline">Culturally Immersive Language Learning Games</p>
    </div>
    <div class="product__stripe product__stripe--right"></div>
    <p class="product__website">www.lumidrasc.example</p>
  </section>

</main>
</body>
</html>
```